C2C website is looking for a web-designer

Complete description of the project you will find in the file atteched (we updated information there and maybe now it will be easier to understand what it's all about). We are a small team of two people from the Czech Republic and we want to create a united platform in the form of adverts, where people can find smb who will help them to cope with the everyday routine (cooking, cleaning, pet care, house work etc.)
Updates
Project Deadline Extended Reason: We want the designers to have more time for work. Added Wednesday, September 24, 2014
This brief depends on brief 416290 - http://tasks.plumvexa.com/task.aspx?id=416290 (logo design). Both are for the same project. Added Wednesday, September 24, 2014
Industry/Entity Type
House
Number of Pages Required
5+ page
Look and feel
Each slider illustrates characteristics of the customer's brand and the style your logo design should communicate.

```html
<!DOCTYPE html>
<html lang="en">
<head>
<meta charset="utf-8">
<title>Handly – Zurich's Largest Marketplace</title>
<link href="https://fonts.googleapis.com/css2?family=Open+Sans:wght@400;600;700&display=swap" rel="stylesheet">
<style>
  :root{
    --topbar:#2f2f2f;
    --page:#efeeee;
    --sidebar:#f2eff0;
    --purple:#5e4a8e;
    --purple-soft:#6b56a3;
    --salmon:#f0887b;
    --salmon-soft:#f3968c;
    --teal:#3fb2c3;
    --teal-soft:#52bfcd;
    --red:#d9262b;
    --ink:#3a3a3a;
    --ad:#efebec;
    --card-sky:#cfe6ec;
  }
  *{box-sizing:border-box;margin:0;padding:0}
  html,body{width:1200px;height:900px;overflow:hidden}
  body{background:var(--page);font-family:"Open Sans",sans-serif;color:var(--ink);position:relative}

  .topbar{position:absolute;left:0;top:0;width:1200px;height:26px;background:var(--topbar)}
  .topnav{position:absolute;left:154px;top:0;display:flex;gap:22px;line-height:27px;font-size:10.5px;color:#eee}
  .account{position:absolute;left:961px;top:3px;display:flex;gap:14px;align-items:center;font-size:11px;color:#fff}
  .account .join{background:var(--salmon);padding:2px 9px;font-size:10.5px}

  .sidebar{position:absolute;left:135px;top:26px;width:263px;height:874px;background:var(--sidebar);box-shadow:2px 0 4px rgba(0,0,0,.08)}
  .brand{height:95px;background:#fbfafa;display:flex;align-items:center;gap:10px;padding-left:22px}
  .brand-dot{width:46px;height:46px;border-radius:50%;background:var(--red)}
  .brand-name{font-size:36px;font-weight:600;color:var(--ink)}
  .categories-title{font-size:25px;color:var(--red);padding:4px 0 0 18px;height:51px;letter-spacing:.5px}
  .category-list{list-style:none}
  .category{position:relative;height:44px;display:flex;align-items:center;padding-left:22px;font-size:12px;border-left:3px solid var(--purple);width:252px}
  .category svg{width:22px;height:22px;margin-right:14px}
  .category.purple{border-color:var(--purple);color:var(--purple)}
  .category.salmon{border-color:var(--salmon);color:var(--salmon)}
  .category.teal{border-color:var(--teal);color:var(--teal)}
  .category.active{background:var(--purple);color:#fff;border-left-color:var(--purple);border-bottom:4px solid #9b8bc2}
  .sidebar-footer{position:absolute;left:22px;top:858px;width:219px;height:20px;background:#d5d3d4}

  .ad-slot{position:absolute;left:417px;top:35px;width:640px;height:77px;background:var(--ad);display:flex;align-items:center;justify-content:center;font-size:13px;color:#777}
  .hero{position:absolute;left:398px;top:120px;width:666px;height:273px}
  .hero-photo{position:absolute;inset:0;background:linear-gradient(180deg,#7fa9d6 0%,#9db2c6 35%,#8e8e8c 60%,#b28a7c 78%,#4e6c7e 100%)}
  .hero-title{position:absolute;left:0;width:100%;top:26px;text-align:center;color:#fff;font-size:42px;font-weight:400;letter-spacing:-.5px;text-shadow:0 1px 3px rgba(0,0,0,.35)}
  .hero-sub{position:absolute;left:0;width:100%;top:84px;text-align:center;color:#fff;font-size:14px;text-shadow:0 1px 2px rgba(0,0,0,.4)}
  .search{position:absolute;left:93px;top:118px;display:flex;height:51px}
  .search-field{width:389px;background:#fff;font-size:15px;color:#888;padding:0 18px;display:flex;align-items:center}
  .search-button{width:122px;background:var(--salmon);color:#fff;font-size:15px;display:flex;align-items:center;justify-content:center}

  .step{position:absolute;top:324px;width:136px;height:136px;border-radius:50%;color:#fff;text-align:center;font-size:12.5px;line-height:16px;display:flex;flex-direction:column;align-items:center;padding-top:28px}
  .step svg{width:36px;height:36px;margin-bottom:12px}
  .step.submit{left:427px;background:var(--purple-soft)}
  .step.offers{left:679px;background:var(--salmon-soft)}
  .step.sold{left:913px;background:var(--teal-soft)}

  .features{position:absolute;left:616px;top:520px;width:263px;height:53px;background:linear-gradient(90deg,#f1868a,#f4a37f);color:#fff;text-align:center;box-shadow:0 2px 4px rgba(0,0,0,.12)}
  .features h2{font-size:23px;font-weight:400;line-height:26px;padding-top:6px;letter-spacing:-.3px}
  .features p{font-size:7px;font-weight:600}

  .card{position:absolute;width:195px;background:linear-gradient(180deg,#e4f1f4,var(--card-sky))}
  .card-photo{width:100%;height:100%}
  .card.one{left:427px;top:632px;height:268px}
  .card.one .card-photo{height:208px}
  .card.two{left:650px;top:632px;height:208px}
  .card.three{left:871px;top:632px;height:208px}
  .card.four{left:650px;top:868px;height:32px}
  .card.five{left:871px;top:868px;height:32px}
  .card-tag{position:absolute;left:-18px;top:10px;width:80px;height:14px;background:var(--salmon);color:#fff;font-size:9px;text-align:center;transform:rotate(-45deg)}
  .card-info{height:60px;background:var(--salmon);color:#fff;font-size:12px;line-height:16px;padding:13px 10px}
</style>
</head>
<body>
  <header class="topbar">
    <nav class="topnav"><span>How it Work</span><span>Become a Trusted Dealer</span><span>Help</span><span>Post an Ad</span><span>Sign In</span></nav>
    <div class="account"><span>Sign In</span><span class="join">Join</span></div>
  </header>

  <aside class="sidebar">
    <div class="brand"><span class="brand-dot"></span><span class="brand-name">Handly</span></div>
    <h2 class="categories-title">Categories</h2>
    <ul class="category-list">
      <li class="category active"><svg viewBox="0 0 22 22"><rect x="3" y="9" width="16" height="10" rx="2" fill="#fff"/><rect x="1" y="7" width="20" height="2" fill="#fff"/></svg>Cooking</li>
      <li class="category salmon"><svg viewBox="0 0 22 22"><circle cx="11" cy="11" r="8" fill="none" stroke="currentColor" stroke-width="2"/></svg>Housework</li>
      <li class="category teal"><svg viewBox="0 0 22 22"><rect x="3" y="8" width="14" height="10" rx="3" fill="currentColor"/></svg>Work in the Garden</li>
      <li class="category purple"><svg viewBox="0 0 22 22"><circle cx="11" cy="11" r="8" fill="currentColor"/></svg>Pet Care</li>
      <li class="category salmon"><svg viewBox="0 0 22 22"><circle cx="11" cy="7" r="4" fill="currentColor"/><rect x="6" y="12" width="10" height="9" rx="3" fill="currentColor"/></svg>Babysitting</li>
      <li class="category teal"><svg viewBox="0 0 22 22"><rect x="6" y="3" width="14" height="10" fill="none" stroke="currentColor" stroke-width="2"/><rect x="2" y="8" width="4" height="12" fill="currentColor"/></svg>Tutoring</li>
      <li class="category purple"><svg viewBox="0 0 22 22"><rect x="3" y="6" width="6" height="14" rx="2" fill="currentColor"/><rect x="13" y="6" width="6" height="14" rx="2" fill="currentColor"/></svg>Elderly Care</li>
      <li class="category salmon"><svg viewBox="0 0 22 22"><rect x="2" y="8" width="18" height="8" rx="3" fill="currentColor"/></svg>Transportation</li>
      <li class="category teal"><svg viewBox="0 0 22 22"><circle cx="11" cy="6" r="4" fill="currentColor"/><rect x="5" y="11" width="12" height="10" rx="2" fill="currentColor"/></svg>Handyman</li>
      <li class="category purple"><svg viewBox="0 0 22 22"><circle cx="11" cy="6" r="4" fill="currentColor"/><circle cx="5" cy="15" r="4" fill="currentColor"/><circle cx="17" cy="15" r="4" fill="currentColor"/></svg>Consulting</li>
      <li class="category salmon"><svg viewBox="0 0 22 22"><rect x="3" y="5" width="14" height="14" fill="none" stroke="currentColor" stroke-width="2"/><path d="M8 15 L20 3" stroke="currentColor" stroke-width="2"/></svg>Art</li>
      <li class="category teal"><svg viewBox="0 0 22 22"><rect x="2" y="13" width="18" height="5" rx="2" fill="currentColor"/><circle cx="7" cy="8" r="3" fill="currentColor"/></svg>Body Care</li>
      <li class="category purple"><svg viewBox="0 0 22 22"><circle cx="11" cy="13" r="8" fill="currentColor"/></svg>Farming</li>
      <li class="category salmon"><svg viewBox="0 0 22 22"><circle cx="8" cy="12" r="6" fill="currentColor"/><circle cx="15" cy="11" r="6" fill="currentColor" opacity=".8"/></svg>Animal Products</li>
      <li class="category teal"><svg viewBox="0 0 22 22"><path d="M3 5 H19 V10 H16 V20 H6 V10 H3 Z" fill="currentColor"/></svg>Hand-made Goods</li>
      <li class="category purple"><svg viewBox="0 0 22 22"><circle cx="6" cy="5" r="3" fill="currentColor"/><circle cx="16" cy="5" r="3" fill="currentColor"/><rect x="3" y="9" width="6" height="11" fill="currentColor"/><rect x="13" y="9" width="6" height="11" fill="currentColor"/></svg>Others</li>
    </ul>
    <div class="sidebar-footer"></div>
  </aside>

  <div class="ad-slot">728 x 90</div>

  <section class="hero">
    <div class="hero-photo" role="img" aria-label="City skyline with high-rise towers beside a river"></div>
    <h1 class="hero-title">Zurich’s Largest Marketplace</h1>
    <p class="hero-sub">Sell anything from used cars to mobiles, furniture, laptops, clothing &amp; more...</p>
    <div class="search"><div class="search-field">What are you looking for?</div><div class="search-button">Find Services</div></div>
  </section>

  <div class="step submit"><svg viewBox="0 0 36 36"><rect x="3" y="5" width="24" height="20" fill="none" stroke="#fff" stroke-width="2"/><path d="M5 23 L12 14 L18 20 L22 16 L26 21" fill="none" stroke="#fff" stroke-width="2"/><circle cx="26" cy="25" r="7" fill="#fff"/><path d="M26 21 V29 M22 25 H30" stroke="var(--purple-soft)" stroke-width="2"/></svg>1. Submit your<br>Ad</div>
  <div class="step offers"><svg viewBox="0 0 36 36"><rect x="6" y="13" width="24" height="18" fill="none" stroke="#fff" stroke-width="2"/><rect x="4" y="9" width="28" height="5" fill="none" stroke="#fff" stroke-width="2"/><path d="M18 9 V31" stroke="#fff" stroke-width="2"/></svg>2. Get Your<br>Offers</div>
  <div class="step sold"><svg viewBox="0 0 36 36"><circle cx="18" cy="18" r="15" fill="none" stroke="#fff" stroke-width="2"/><circle cx="18" cy="18" r="11" fill="none" stroke="#fff" stroke-width="1.5"/><path d="M12 18 L16 22 L24 13" fill="none" stroke="#fff" stroke-width="2.5"/></svg>3. Sold</div>

  <div class="features"><h2>FEATURES ADS</h2><p>CHOOSE FROM OUR MOST POPULAR SERVICES</p></div>

  <article class="card one">
    <div class="card-photo" role="img" aria-label="Black smartphone shown front and side"></div>
    <span class="card-tag">New</span>
    <div class="card-info">Fonix 4GS<br>US. 50,000$</div>
  </article>
  <article class="card two"><div class="card-photo" role="img" aria-label="Red hatchback car"></div></article>
  <article class="card three"><div class="card-photo" role="img" aria-label="Open laptop computer"></div></article>
  <article class="card four"><div class="card-photo" role="img" aria-label="Featured ad item"></div></article>
  <article class="card five"><div class="card-photo" role="img" aria-label="Featured ad item"></div></article>
</body>
</html>
```